Oven Cleaning flyer design

Hi there,
I need help designing a letterbox flyer. It needs to be DL size.
I have attached a rough design made with Chat GPT.
Would like back and front, have my business colors.
Please find attached mock up of what I would roughly like.
Also find attached logo.
Thank you

Target Market(s)

Home owners over 40

Industry/Entity Type

Cleaning

Requirements
Must have
• Logo, before after of oven, brand colors

```html
<!DOCTYPE html>
<html lang="en">
<head>
<meta charset="utf-8">
<title>Bright Oven Care – DL Flyer Front and Back</title>
<link rel="stylesheet" href="https://fonts.googleapis.com/css2?family=Archivo+Black&family=Montserrat:wght@400;500;600&family=Playfair+Display:ital,wght@1,600&family=Poppins:wght@600;700;800&display=swap">
<style>
  :root {
    --stage: #4b4d4d;
    --navy: #19214d;
    --teal: #48c2c9;
    --teal-deep: #1f9aa3;
    --white: #ffffff;
    --ink: #2a2d3a;
    --mist: #eef0f2;
  }
  * { box-sizing: border-box; margin: 0; padding: 0; }
  html, body { width: 1189px; height: 1200px; overflow: hidden; background: var(--stage); }
  .stage { position: relative; width: 1189px; height: 1200px; }
  .side-label {
    position: absolute; top: 34px; width: 300px; text-align: center;
    font-family: "Archivo Black", sans-serif; font-size: 25px; letter-spacing: 9px;
    color: var(--white);
  }
  .side-label.front-label { left: 159px; }
  .side-label.back-label { left: 736px; }

  .flyer {
    position: absolute; top: 75px; width: 505px; height: 1070px;
    background: var(--white); overflow: hidden;
  }
  .flyer.front { left: 68px; }
  .flyer.back { left: 625px; }
  .flyer > svg.backdrop { position: absolute; inset: 0; }

  .brand { position: absolute; left: 50px; top: 52px; display: flex; align-items: center; gap: 14px; }
  .brand-dot { width: 62px; height: 62px; border-radius: 50%; background: var(--teal); }
  .brand-name {
    font-family: "Poppins", sans-serif; font-weight: 800; font-size: 27px;
    line-height: 1; color: var(--navy); letter-spacing: 0.5px;
  }

  .headline { position: absolute; left: 51px; font-family: "Poppins", sans-serif; font-weight: 700; line-height: 1.15; }
  .headline .lead { display: block; color: var(--teal); }
  .headline .strong { display: block; color: var(--navy); }
  .front .headline { top: 148px; font-size: 45px; }
  .back .headline { top: 158px; font-size: 40px; }

  .intro { position: absolute; left: 51px; font-family: "Montserrat", sans-serif; color: var(--ink); }
  .front .intro { top: 256px; width: 370px; font-size: 16.5px; line-height: 20px; }
  .back .intro { top: 262px; width: 420px; font-size: 14.6px; line-height: 18.2px; }

  .photo {
    position: absolute; top: 504px; width: 216px; height: 232px;
    border: 4px solid var(--white); border-radius: 18px; overflow: hidden;
  }
  .photo.before { left: 36px; background: linear-gradient(165deg, #bdbcb6 0%, #2a2826 30%, #141414 55%, #8a6b3d 75%, #3a2f22 100%); }
  .photo.after { left: 259px; background: linear-gradient(165deg, #c6c8c8 0%, #2a2b2d 30%, #111214 55%, #6f7377 75%, #463a2c 100%); }
  .compare-tag {
    position: absolute; left: 170px; top: 600px; height: 40px; width: 170px;
    border-radius: 20px; display: flex; overflow: hidden;
    font-family: "Poppins", sans-serif; font-weight: 700; font-size: 17px;
  }
  .compare-tag span { flex: 1; display: flex; align-items: center; justify-content: center; }
  .compare-tag .tag-before { background: var(--teal); color: var(--white); }
  .compare-tag .tag-after { background: var(--white); color: var(--navy); }

  .offer {
    position: absolute; left: 46px; top: 382px; width: 430px; height: 286px;
    background: var(--navy); border-radius: 20px; color: var(--white);
  }
  .offer-intro {
    position: absolute; top: 18px; left: 0; right: 0; text-align: center;
    font-family: "Montserrat", sans-serif; font-weight: 500; font-size: 20px;
  }
  .offer-intro::before, .offer-intro::after {
    content: ""; display: inline-block; width: 30px; height: 1px; background: var(--white);
    vertical-align: middle; margin: 0 10px;
  }
  .offer-deal {
    position: absolute; top: 40px; left: 0; right: 0; text-align: center;
    font-family: "Poppins", sans-serif; font-weight: 800; font-size: 76px; line-height: 1.15; letter-spacing: -2px;
  }
  .offer-deal .currency { font-size: 32px; color: var(--teal); vertical-align: 30px; margin-right: 6px; }
  .offer-deal .amount { color: var(--teal); }
  .offer-rule { position: absolute; top: 127px; left: 27px; right: 18px; height: 1px; background: rgba(255,255,255,0.55); }
  .perks { position: absolute; top: 142px; left: 16px; right: 16px; display: flex; }
  .perk { flex: 1; text-align: center; font-family: "Montserrat", sans-serif; font-weight: 500; font-size: 13.5px; line-height: 16px; }
  .perk + .perk { border-left: 1px dashed rgba(255,255,255,0.7); }
  .perk svg { display: block; margin: 0 auto 12px; }

  .call-line {
    position: absolute; top: 849px; left: 0; right: 0; text-align: center;
    font-family: "Poppins", sans-serif; font-weight: 700; font-size: 21.5px; color: var(--white);
  }
  .phone-number {
    position: absolute; top: 872px; left: 0; right: 0; text-align: center;
    font-family: "Poppins", sans-serif; font-weight: 700; font-size: 62px; letter-spacing: -1px; color: var(--white);
  }
  .also-line {
    position: absolute; top: 978px; left: 0; right: 0; text-align: center;
    font-family: "Playfair Display", serif; font-style: italic; font-weight: 600; font-size: 21px; color: var(--navy);
  }
  .web-line {
    position: absolute; top: 1019px; left: 0; right: 0; text-align: center;
    font-family: "Montserrat", sans-serif; font-size: 16px; letter-spacing: 3px; color: var(--navy);
    display: flex; align-items: center; justify-content: center; gap: 8px;
  }
</style>
</head>
<body>
<div class="stage">
  <div class="side-label front-label">FRONT</div>
  <div class="side-label back-label">BACK</div>

  <!-- FRONT SIDE -->
  <section class="flyer front">
    <svg class="backdrop" width="505" height="1070" viewBox="0 0 505 1070">
      <defs>
        <linearGradient id="kitchenLight" x1="0" y1="0" x2="0" y2="1">
          <stop offset="0" stop-color="#f7f8f8"/>
          <stop offset="1" stop-color="#e7e9ea"/>
        </linearGradient>
        <linearGradient id="silverLine" x1="0" x2="1">
          <stop offset="0" stop-color="#ffffff"/>
          <stop offset="0.5" stop-color="#1f9aa3"/>
          <stop offset="1" stop-color="#ffffff"/>
        </linearGradient>
      </defs>
      <rect width="505" height="560" fill="url(#kitchenLight)" role="img" aria-label="Faded photo of a bright modern kitchen with an oven"/>
      <path d="M505,200 C490,330 300,480 70,505 C30,510 0,495 0,470 L0,1070 L505,1070 Z" fill="var(--navy)"/>
      <path d="M398,118 C500,130 525,220 470,300 C400,410 220,510 70,508 C18,506 10,450 28,400" fill="none" stroke="var(--teal)" stroke-width="15" stroke-linecap="round"/>
      <path d="M418,360 l8,-28 l8,28 l28,8 l-28,8 l-8,28 l-8,-28 l-28,-8 Z" fill="#fff"/>
      <path d="M374,410 l5,-18 l5,18 l18,5 l-18,5 l-5,18 l-5,-18 l-18,-5 Z" fill="#fff"/>
      <path d="M0,772 Q252,842 505,772 L505,963 L0,963 Z" fill="var(--teal)"/>
      <path d="M20,790 Q252,838 490,790" fill="none" stroke="url(#silverLine)" stroke-width="4"/>
      <path d="M48,810 l6,-26 l6,26 l26,6 l-26,6 l-6,26 l-6,-26 l-26,-6 Z" fill="#fff"/>
      <path d="M92,832 l4,-14 l4,14 l14,4 l-14,4 l-4,14 l-4,-14 l-14,-4 Z" fill="#fff"/>
      <circle cx="250" cy="800" r="43" fill="var(--navy)" stroke="var(--teal)" stroke-width="5"/>
      <g fill="#fff">
        <path d="M224,792 q26,-18 52,0 v6 h-12 v-5 q-14,-5 -28,0 v5 h-12 Z"/>
        <path d="M234,800 h32 l8,20 h-48 Z"/>
      </g>
      <circle cx="250" cy="810" r="6" fill="var(--navy)"/>
    </svg>

    <div class="brand"><div class="brand-dot"></div><div class="brand-name">BRIGHT OVEN CARE</div></div>
    <h1 class="headline"><span class="lead">Bring Your Oven</span><span class="strong">Back to Life</span></h1>
    <p class="intro">Professional, non-caustic oven cleaning that removes built-up grease, smoke and burnt grime-leaving your oven looking fresh again.</p>

    <div class="photo before" role="img" aria-label="Photo of a greasy, stained oven interior before cleaning"></div>
    <div class="photo after" role="img" aria-label="Photo of the same oven interior clean after service"></div>
    <div class="compare-tag"><span class="tag-before">BEFORE</span><span class="tag-after">AFTER</span></div>

    <p class="call-line">Call Now for Fast, Professional Service</p>
    <p class="phone-number">0400 528 193</p>
    <p class="also-line">We also clean&nbsp; cooktops, rangehoods and BBQs</p>
    <p class="web-line">
      <svg width="18" height="18" viewBox="0 0 20 20" fill="none" stroke="var(--navy)" stroke-width="1.5"><circle cx="10" cy="10" r="8.5"/><ellipse cx="10" cy="10" rx="4" ry="8.5"/><path d="M1.5 10h17M3 5.5h14M3 14.5h14"/></svg>
      www.brightovencare.com.au
    </p>
  </section>

  <!-- BACK SIDE -->
  <section class="flyer back">
    <svg class="backdrop" width="505" height="1070" viewBox="0 0 505 1070">
      <defs>
        <linearGradient id="kitchenBack" x1="0" y1="0" x2="0" y2="1">
          <stop offset="0" stop-color="#f5f6f7"/>
          <stop offset="0.6" stop-color="#eceeef"/>
          <stop offset="1" stop-color="#d9dcde"/>
        </linearGradient>
        <linearGradient id="silverLineB" x1="0" x2="1">
          <stop offset="0" stop-color="#ffffff"/>
          <stop offset="0.5" stop-color="#1f9aa3"/>
          <stop offset="1" stop-color="#ffffff"/>
        </linearGradient>
      </defs>
      <rect width="505" height="800" fill="url(#kitchenBack)" role="img" aria-label="Faded photo of a white kitchen with a gas cooktop and oven"/>
      <path d="M0,772 Q252,842 505,772 L505,963 L0,963 Z" fill="var(--teal)"/>
      <path d="M20,790 Q252,838 490,790" fill="none" stroke="url(#silverLineB)" stroke-width="4"/>
      <path d="M70,812 l6,-26 l6,26 l26,6 l-26,6 l-6,26 l-6,-26 l-26,-6 Z" fill="#fff"/>
      <path d="M37,838 l4,-14 l4,14 l14,4 l-14,4 l-4,14 l-4,-14 l-14,-4 Z" fill="#fff"/>
      <circle cx="252" cy="800" r="43" fill="var(--navy)" stroke="var(--teal)" stroke-width="5"/>
      <g fill="#fff">
        <path d="M226,792 q26,-18 52,0 v6 h-12 v-5 q-14,-5 -28,0 v5 h-12 Z"/>
        <path d="M236,800 h32 l8,20 h-48 Z"/>
      </g>
      <circle cx="252" cy="810" r="6" fill="var(--navy)"/>
    </svg>

    <div class="brand"><div class="brand-dot"></div><div class="brand-name">BRIGHT OVEN CARE</div></div>
    <h2 class="headline"><span class="lead">Why Choose</span><span class="strong">Bright Oven Care?</span></h2>
    <p class="intro">We’re a local family business providing professional, non-caustic oven cleaning across Sunshine Coast. Using specialized equipment and proven cleaning methods, we remove heavy grease, carbon build-up, smoke residue, restoring your oven safely and effectively.</p>

    <div class="offer">
      <svg width="60" height="60" viewBox="0 0 60 60" style="position:absolute;right:8px;top:-2px">
        <path d="M36,26 l5,-20 l5,20 l20,5 l-20,5 l-5,20 l-5,-20 l-20,-5 Z" fill="#fff"/>
        <path d="M14,36 l3,-11 l3,11 l11,3 l-11,3 l-3,11 l-3,-11 l-11,-3 Z" fill="#fff"/>
      </svg>
      <p class="offer-intro">Mention this flyer for</p>
      <p class="offer-deal"><span class="currency">$</span><span class="amount">10%</span> OFF</p>
      <div class="offer-rule"></div>
      <div class="perks">
        <div class="perk">
          <svg width="78" height="78" viewBox="0 0 78 78" fill="none" stroke-width="2">
            <circle cx="39" cy="39" r="37" stroke="#fff"/>
            <circle cx="36" cy="39" r="17" stroke="#fff" stroke-dasharray="6 3"/>
            <path d="M36,48 v-14 l6,-8 q4,0 3,5 l-1,5 h8 q4,0 3,4 l-2,9 q-1,3 -4,3 h-13 Z" stroke="var(--teal)"/>
          </svg>
          Reliable Service
        </div>
        <div class="perk">
          <svg width="78" height="78" viewBox="0 0 78 78" fill="none" stroke-width="2">
            <circle cx="39" cy="39" r="37" stroke="#fff"/>
            <rect x="22" y="22" width="30" height="36" rx="5" transform="rotate(35 37 40)" stroke="#fff"/>
            <path d="M26,52 l12,-14 l4,4 l-10,14" stroke="var(--teal)"/>
            <path d="M55,20 l2,-6 l2,6 l6,2 l-6,2 l-2,6 l-2,-6 l-6,-2 Z" stroke="#fff"/>
          </svg>
          Non-Caustic<br>Cleaning
        </div>
        <div class="perk">
          <svg width="78" height="78" viewBox="0 0 78 78" fill="none" stroke-width="2">
            <circle cx="39" cy="39" r="37" stroke="#fff"/>
            <path d="M20,54 a19,19 0 0 1 38,0" stroke="#fff"/>
            <path d="M39,54 l12,-14" stroke="var(--teal)" stroke-width="3"/>
            <rect x="30" y="18" width="18" height="12" rx="2" stroke="#fff"/>
            <path d="M33,27 l4,-4 l3,3 l5,-5" stroke="var(--teal)"/>
          </svg>
          Satisfaction<br>Guaranteed
        </div>
      </div>
    </div>

    <p class="call-line">Call Now for Fast, Professional Service</p>
    <p class="phone-number">0400 528 193</p>
    <p class="also-line">We also clean&nbsp; cooktops, rangehoods and BBQs</p>
    <p class="web-line">
      <svg width="18" height="18" viewBox="0 0 20 20" fill="none" stroke="var(--navy)" stroke-width="1.5"><circle cx="10" cy="10" r="8.5"/><ellipse cx="10" cy="10" rx="4" ry="8.5"/><path d="M1.5 10h17M3 5.5h14M3 14.5h14"/></svg>
      www.brightovencare.com.au
    </p>
  </section>
</div>
</body>
</html>
```